Ternhollow Partners

Need a new website - see more on ternhollowpartners.example

Target Market(s)

Finance industry = conservative design

Coding

Coded - Design and coding required

Number of Pages Required

5+ page

Requirements
Should not have
• Dear all,
• Please avoid pictures of people on the website (except the "team" of course :-)

```html
<!DOCTYPE html>
<html lang="en">
<head>
<meta charset="utf-8">
<title>Ternhollow Partners</title>
<link href="https://fonts.googleapis.com/css2?family=Poppins:wght@300;400;500;600;700&display=swap" rel="stylesheet">
<style>
:root{
  --red:#c8101e;
  --ink:#1b1b1b;
  --grey:#9a9a9a;
  --mid:#555;
  --hero:#ebebeb;
  --line:#bdbdbd;
  --white:#fff;
}
*{margin:0;padding:0;box-sizing:border-box}
html,body{width:702px;height:1200px;overflow:hidden;background:var(--white)}
body{font-family:'Poppins',sans-serif;color:var(--ink);position:relative}

.header{position:absolute;left:0;top:0;width:702px;height:68px;background:var(--white)}
.brand-name{position:absolute;left:94px;top:25px;font-weight:600;font-size:15px;line-height:18px;color:var(--ink);white-space:nowrap}
.nav{position:absolute;top:29px;font-size:7.3px;font-weight:500;color:var(--ink);white-space:nowrap}
.nav.active{color:var(--red)}

.hero{position:absolute;left:0;top:68px;width:702px;height:323px;background:var(--hero)}
.hero-line{position:absolute;left:94px;font-size:17.5px;line-height:20px;font-weight:500;white-space:nowrap}
.muted{color:var(--grey);font-weight:400}
.hero-big{position:absolute;left:94px;font-size:31px;line-height:34px;font-weight:700;letter-spacing:.3px}
.dots{position:absolute;left:94px;top:245px;display:flex;gap:3px}
.dots span{width:6px;height:6px;border-radius:50%;background:#8a8a8a}
.dots span:first-child{background:var(--red)}
.hero-art{position:absolute;left:348px;top:20px;width:256px;height:256px;border-radius:50%;
  background:radial-gradient(circle,#f2f2f2 0 34%,#d9d9d9 35% 55%,#c7c7c7 56% 100%)}
.scroll-btn{position:absolute;left:340px;top:283px;width:20px;height:20px;border-radius:50%;background:var(--white)}

.service{position:absolute;top:434px;height:156px;border-left:2px solid var(--line);padding-left:8px}
.service-icon{width:66px;height:66px;border-radius:50%;background:var(--red);margin-left:1px;margin-top:-8px}
.service h3{font-size:11.5px;line-height:14px;font-weight:500;margin-top:10px}
.service p{font-size:6.5px;line-height:12px;color:var(--mid);margin-top:8px}

.about-title{position:absolute;left:94px;top:644px;font-size:19.5px;font-weight:600;white-space:nowrap}
.about-col{position:absolute;top:684px;width:134px;font-size:6.5px;line-height:11.8px;color:var(--ink)}
.about-col p{margin-bottom:11.8px}
.about-shadow{position:absolute;left:434px;top:667px;width:170px;height:210px;background:var(--ink)}
.about-photo{position:absolute;left:408px;top:641px;width:186px;height:228px;
  background:linear-gradient(135deg,#c20d1a,#ee2a2a 55%,#d8141f)}

.contact-rule{position:absolute;left:63px;top:933px;width:2px;height:267px;background:var(--red)}
.contact-title{position:absolute;left:94px;top:952px;font-size:19.5px;font-weight:600}
.offices{position:absolute;left:94px;top:1002px;font-size:13px;font-weight:600;color:var(--red)}
.offices-text{position:absolute;left:94px;top:1024px;width:118px;font-size:7.4px;line-height:12.8px;color:#333}
.field{position:absolute;border-bottom:1px solid #7d7d7d;font-size:7.5px;color:#777;padding-left:8px}
.submit{position:absolute;left:551px;top:1110px;width:56px;height:22px;background:var(--red);color:var(--white);
  font-size:7.5px;font-weight:600;letter-spacing:.8px;text-align:center;line-height:22px}
.footer-rule{position:absolute;left:94px;top:1153px;width:513px;height:1px;background:#cfcfcf}
.copyright{position:absolute;left:99px;top:1175px;font-size:6.6px;color:var(--ink);white-space:nowrap}
.copyright em{font-style:normal;color:var(--red)}
.social{position:absolute;top:1171px;width:18px;height:18px;border-radius:50%;background:#a9a9a9}
</style>
</head>
<body>

<header class="header">
  <div class="brand-name">Ternhollow Partners</div>
  <span class="nav active" style="left:328px">Home</span>
  <span class="nav" style="left:366px">Services</span>
  <span class="nav" style="left:411px">Current Engagements</span>
  <span class="nav" style="left:506px">News</span>
  <span class="nav" style="left:541px">Team</span>
  <span class="nav" style="left:578px">Contact</span>
</header>

<section class="hero">
  <div class="hero-line" style="top:82px">Ternhollow <span class="muted">Partners</span></div>
  <div class="hero-line muted" style="top:102px">is a privately held</div>
  <div class="hero-big" style="top:128px">GLOBAL</div>
  <div class="hero-big" style="top:164px;color:var(--red)">INVESTMENT</div>
  <div class="hero-line" style="top:197px"><span class="muted">holding</span> Group</div>
  <div class="dots"><span></span><span></span><span></span><span></span></div>
  <div class="hero-art" role="img" aria-label="Illustration of a team standing in a circle around a red target emblem"></div>
  <div class="scroll-btn">
    <svg width="20" height="20" viewBox="0 0 20 20"><path d="M6.5 8.5 10 12l3.5-3.5" fill="none" stroke="#c8101e" stroke-width="1.8"/></svg>
  </div>
</section>

<section>
  <div class="service" style="left:95px;width:160px">
    <div class="service-icon"><svg width="66" height="66" viewBox="0 0 66 66"><g fill="none" stroke="#fff" stroke-width="1.6"><rect x="24" y="19" width="19" height="26"/><path d="M28 26h11M28 31h11M28 36h11M28 41h7"/></g></svg></div>
    <h3>Private<br>Placements</h3>
    <p>Ternhollow Partners efficiently arranges both equity and debt financing by offering new capital to public and private companies.</p>
  </div>
  <div class="service" style="left:282px;width:158px">
    <div class="service-icon"><svg width="66" height="66" viewBox="0 0 66 66"><g fill="#fff"><circle cx="26" cy="37" r="4"/><circle cx="40" cy="37" r="4"/><path d="M19 48a7 6 0 0 1 14 0zM33 48a7 6 0 0 1 14 0z"/></g><text x="33" y="31" fill="#fff" font-family="Poppins,sans-serif" font-size="14" font-weight="600" text-anchor="middle">$</text></svg></div>
    <h3>Reverse Mergers &amp;<br>Alternative Offerings</h3>
    <p>Ternhollow Partners assists fast growing privately-held companies with easy and affordable access to the public markets in the U.S.</p>
  </div>
  <div class="service" style="left:464px;width:150px">
    <div class="service-icon"><svg width="66" height="66" viewBox="0 0 66 66"><g fill="none" stroke="#fff" stroke-width="1.6"><path d="M20 47h27"/><rect x="23" y="39" width="5" height="8"/><rect x="31" y="34" width="5" height="13"/><rect x="39" y="29" width="5" height="18"/><path d="M21 33l9-6 6 3 9-10M41 20h4v4"/></g></svg></div>
    <h3>Mergers &amp;<br>Acquisitions</h3>
    <p>We advise in mergers &amp; acquisitions, roll-up strategies, joint ventures, recapitalizations, operate restructuring, and spin-offs.</p>
  </div>
</section>

<section>
  <h2 class="about-title"><span style="color:#555;font-weight:600">About</span> Ternhollow partners</h2>
  <div class="about-col" style="left:96px">
    <p>Sed ut perspiciatis unde omnis iste natus error sit voluptatem accusantium doloremque laudantium, totam rem aperiam, eaque ipsa quae ab illo inven tore veritatis et quasi architecto beatae vitae dicta sunt explicabo.</p>
    <p>Dsam voluptatem quia voluptas sit aspernatur aut odit aut fugit, sed quia consequuntur magni dolores eos qui ratione voluptatem sequi nesciunt.eq ue porro quisquam est,</p>
    <p>Sui dolorem psum quia dolor sit amet, consectetur, adipisci velit, sed quia non numquam</p>
  </div>
  <div class="about-col" style="left:250px">
    <p>Sed ut perspiciatis unde omnis iste natus error sit voluptatem accusantium doloremque laudantium, totam rem aperiam, eaque ipsa quae ab illo inven tore veritatis et quasi architecto beatae vitae dicta sunt explicabo.emo enim am voluptatem quia voluptas sit aspernatur aut odit aut fugit, sed quia consequuntur magni dolores eos qui ratione voluptam sequi nesciunt.</p>
    <p>Prro quisquam est, qui dolorem psum quia dolor sit amet, consectetur, adipisci velit, sed quia non numquam eius modi tempora incidun</p>
  </div>
  <div class="about-shadow"></div>
  <div class="about-photo" role="img" aria-label="Photo of two business people shaking hands, tinted red"></div>
</section>

<section>
  <div class="contact-rule"></div>
  <h2 class="contact-title"><span style="color:#555">Contact</span> Us</h2>
  <div class="offices">Offices</div>
  <p class="offices-text">Founded in 2004, Ternhollow is headquarterd in Gibraltar with representative offices in Luxembourg and London.</p>
  <div class="field" style="left:244px;top:996px;width:152px;height:20px">Full name</div>
  <div class="field" style="left:244px;top:1034px;width:152px;height:20px">E-mail</div>
  <div class="field" style="left:244px;top:1073px;width:152px;height:20px">Phone</div>
  <div class="field" style="left:410px;top:996px;width:196px;height:96px">Your message...</div>
  <div class="submit">SUBMIT</div>
</section>

<footer>
  <div class="footer-rule"></div>
  <p class="copyright">© 2018 <em>Ternhollow Partners</em>.All rights are reserved. Privacy | Terms of use</p>
  <span class="social" style="left:525px"></span>
  <span class="social" style="left:546px"></span>
  <span class="social" style="left:567px"></span>
  <span class="social" style="left:588px"></span>
</footer>

</body>
</html>
```